New Business Card

Use website for color, logo and theme.

http://www.brightlanehomes.com/

Back side of card should be programs listed on home page of website

1) Phone Number is (800) 419-6625 x42
2) Fax (240) 357-8846
3) Address is - 645 W Harwell Avenue, Suite 312, Baltimore, MD 21201
4) NMLS #371846

```html
<!DOCTYPE html>
<html lang="en">
<head>
<meta charset="utf-8">
<title>Bright Lane Financial – Business Card</title>
<link rel="stylesheet" href="https://fonts.googleapis.com/css2?family=Open+Sans:wght@400;600;700&display=swap">
<style>
  :root {
    --gold: #a9992f;
    --gold-light: #c8b95a;
    --blue: #1f4fa3;
    --blue-dark: #163d86;
    --ink: #4a4a4a;
    --paper: #ffffff;
    --backdrop: #e9e7e2;
  }
  * { box-sizing: border-box; margin: 0; padding: 0; }
  html, body { width: 1200px; height: 913px; overflow: hidden; }
  body {
    background: var(--backdrop);
    font-family: "Open Sans", Arial, sans-serif;
    position: relative;
  }
  .card {
    position: absolute;
    width: 540px;
    height: 309px;
    background: var(--paper);
    border-radius: 16px;
    overflow: hidden;
    box-shadow: 0 10px 30px rgba(0,0,0,.18);
  }
  .card-front { left: 60px; top: 110px; }
  .card-back { left: 600px; top: 480px; }
  .card-art { position: absolute; inset: 0; }

  /* front */
  .identity { position: absolute; right: 28px; top: 22px; text-align: right; }
  .identity-name { color: var(--gold); font-weight: 700; font-size: 22px; line-height: 1.1; }
  .identity-role { color: var(--blue); font-size: 14px; }
  .identity-license { color: var(--gold-light); font-size: 14px; }

  .brand { position: absolute; display: flex; align-items: center; gap: 8px; }
  .brand-dot { width: 26px; height: 26px; border-radius: 50%; background: var(--blue); flex: none; }
  .brand-name { color: var(--gold); font-weight: 700; font-size: 17px; line-height: 1.1; }
  .card-front .brand { left: 26px; top: 118px; }

  .address { position: absolute; left: 26px; top: 172px; color: var(--gold); font-size: 14px; line-height: 1.3; }
  .contact { position: absolute; left: 26px; top: 218px; list-style: none; color: var(--gold); font-size: 14px; line-height: 1.4; }
  .contact li { display: flex; align-items: center; gap: 8px; }
  .contact svg { width: 11px; height: 11px; fill: var(--blue); flex: none; }

  /* back */
  .card-back .brand { left: 50%; top: 40px; transform: translateX(-50%); }
  .card-back .brand-name { font-size: 20px; }
  .rule { position: absolute; left: 150px; right: 150px; top: 92px; height: 1px; background: var(--blue); opacity: .5; }
  .headline {
    position: absolute; left: 0; right: 0; top: 104px; text-align: center;
    color: var(--gold); font-weight: 600; font-size: 15px; line-height: 1.3; text-transform: uppercase;
  }
  .programs {
    position: absolute; left: 30px; top: 152px; list-style: none;
    color: var(--gold); font-size: 15px; line-height: 1.45;
  }
  .programs li { display: inline-flex; align-items: center; gap: 6px; margin-right: 8px; }
  .programs li::before { content: ""; width: 10px; height: 10px; border-radius: 50%; background: var(--blue-dark); }
</style>
</head>
<body>

<section class="card card-front" aria-label="Business card front">
  <svg class="card-art" viewBox="0 0 540 309" aria-hidden="false">
    <defs>
      <linearGradient id="portraitTone" x1="0" y1="0" x2="0" y2="1">
        <stop offset="0" stop-color="#8a6a55"/>
        <stop offset="1" stop-color="#1e1e24"/>
      </linearGradient>
    </defs>
    <rect role="img" aria-label="Portrait photo of the loan officer in a suit" x="330" y="85" width="175" height="150" fill="url(#portraitTone)"/>
    <path d="M520 0 A40 40 0 0 0 540 36 L540 0 Z" fill="var(--blue)"/>
    <path d="M190 309 C300 280 420 225 540 150 L540 309 Z" fill="var(--gold)"/>
    <path d="M210 300 C320 262 430 205 540 132 L540 146 C430 218 320 270 210 300 Z" fill="var(--blue)"/>
  </svg>

  <div class="identity">
    <p class="identity-name">Dale Marsh</p>
    <p class="identity-role">Owner</p>
    <p class="identity-license">NMLS #371846</p>
  </div>

  <div class="brand">
    <span class="brand-dot"></span>
    <span class="brand-name">Bright Lane Financial</span>
  </div>

  <p class="address">645 W Harwell Avenue<br>Suite 312, Baltimore, MD 21201</p>

  <ul class="contact">
    <li><svg viewBox="0 0 10 10"><circle cx="3" cy="3" r="2.4"/><circle cx="7" cy="3" r="2.4"/><circle cx="5" cy="7" r="2.4"/></svg>(240) 357-8846</li>
    <li><svg viewBox="0 0 10 10"><path d="M2 0.5 L4 0.5 L4.6 3 L3.4 4 Q4.5 6 6 6.6 L7 5.4 L9.5 6 L9.5 8 Q9.5 9.5 8 9.5 Q0.5 9 0.5 2 Q0.5 0.5 2 0.5 Z"/></svg>(800) 419-6625 x42</li>
    <li><svg viewBox="0 0 10 10"><circle cx="5" cy="5" r="4.5"/></svg>www.brightlanehomes.com</li>
  </ul>
</section>

<section class="card card-back" aria-label="Business card back">
  <svg class="card-art" viewBox="0 0 540 309">
    <path d="M250 309 C380 285 470 230 540 130 L540 309 Z" fill="var(--blue)"/>
    <path d="M230 300 C370 268 460 210 530 120" fill="none" stroke="var(--gold)" stroke-width="3"/>
  </svg>

  <div class="brand">
    <span class="brand-dot"></span>
    <span class="brand-name">Bright Lane Financial</span>
  </div>
  <div class="rule"></div>

  <p class="headline">Check out our<br>exciting new product line</p>

  <ul class="programs">
    <li>Traditional Loan Programs</li>
    <li>Low Credit Score Programs</li>
    <li>Alternative Loan Programs</li>
  </ul>
</section>

</body>
</html>
```